Wollondilly ridge aerial works business card size advertising

I’m after a simple design , please see attached photo . Im after the same color green in the photo as the base color and the the little white man but instead of him holding a spanner i would like him to be holding a tv antenna pointing an angle , see attached photo of the antenna , i would like him on the left of the business card and the business name to fit in on the right with the phone number . ( if the antenna idea looks stupid , leave him holding a spanner ) On the reverse side of the card i would like a white background with green writing stating some of the services we provide which are the following .Antenna installations and repairs Wall mounting of tv’s Additional TV outlets Brolga satellite supply and installations Goulburn , Crookwell , Taralga , Tarago , Marulan , Collector , All rural areas All in all i would like the business card to compliment my invoices as pictured “ invoice supplied is a dummy invoice “

Contact Information for Business Card

wollondilly ridge aerial works 0418563927

Font styles to use
Sans Serif

Colors
9bcb3c

Requirements
Must have
• what i ask for in project description

```html
<!DOCTYPE html>
<html lang="en">
<head>
<meta charset="utf-8">
<title>Wollondilly Ridge Aerial Works – Business Card</title>
<link rel="stylesheet" href="https://fonts.googleapis.com/css2?family=Raleway:wght@400;600;700&family=Open+Sans:wght@400;600&display=swap">
<style>
  :root {
    --brand-green: #9bcb3c;
    --ink: #3a3a3a;
    --card: #ffffff;
    --backdrop: #2b2b2b;
  }
  * { box-sizing: border-box; margin: 0; padding: 0; }
  html, body { width: 1200px; height: 900px; overflow: hidden; }
  body {
    background: var(--backdrop);
    display: flex;
    align-items: center;
    justify-content: center;
    gap: 40px;
    font-family: "Open Sans", sans-serif;
  }
  .card {
    position: relative;
    width: 540px;
    height: 309px;
    background: var(--card);
    border-radius: 18px;
    overflow: hidden;
    box-shadow: 0 8px 24px rgba(0,0,0,.35);
  }
  .brand-mark {
    position: absolute;
    width: 120px;
    height: 120px;
    background: var(--brand-green);
  }
  .business-name {
    position: absolute;
    font-family: "Raleway", sans-serif;
    line-height: 1.05;
  }
  .business-name .primary {
    display: block;
    font-weight: 700;
    color: var(--ink);
    letter-spacing: .04em;
    text-transform: uppercase;
  }
  .business-name .secondary {
    display: block;
    font-weight: 400;
    color: var(--brand-green);
    letter-spacing: .03em;
    text-transform: uppercase;
  }

  /* Front */
  .card-front .brand-mark { left: 210px; top: 48px; }
  .card-front .business-name { left: 150px; top: 176px; }
  .card-front .primary { font-size: 22px; }
  .card-front .secondary { font-size: 21px; }
  .phone {
    position: absolute;
    left: 134px;
    top: 232px;
    display: flex;
    align-items: center;
    gap: 8px;
    font-family: "Raleway", sans-serif;
    font-size: 28px;
    color: var(--ink);
    letter-spacing: .02em;
  }
  .phone svg { width: 16px; height: 22px; fill: var(--brand-green); }

  /* Back */
  .card-back .brand-mark { left: 210px; top: 30px; }
  .card-back .business-name { left: 200px; top: 156px; }
  .card-back .primary { font-size: 19px; }
  .card-back .secondary { font-size: 18px; }
  .services {
    position: absolute;
    left: 40px;
    right: 40px;
    top: 206px;
    text-align: center;
    font-size: 12.5px;
    line-height: 1.45;
    color: var(--ink);
  }
  .service-areas {
    position: absolute;
    left: 0;
    right: 0;
    bottom: 26px;
    height: 22px;
    background: var(--brand-green);
    color: #fff;
    font-size: 11.5px;
    line-height: 22px;
    text-align: center;
  }
</style>
</head>
<body>
  <section class="card card-front" aria-label="Business card front">
    <div class="brand-mark"></div>
    <h1 class="business-name">
      <span class="primary">Wollondilly Ridge</span>
      <span class="secondary">Aerial Works</span>
    </h1>
    <p class="phone">
      <svg viewBox="0 0 16 22" aria-hidden="true"><path d="M4 1c1 0 2 .5 2.3 1.5l1 3.5c.2.8-.1 1.6-.8 2L5 9c.6 2 1.7 3.8 3.2 5.2l1.6-1c.7-.4 1.6-.3 2.1.3l2.3 2.6c.6.7.5 1.8-.2 2.4l-1.5 1.3C10.4 21.5 6 18 3.2 13.2.6 8.7.4 4.2 1.6 2.2 2.2 1.4 3 1 4 1z"/></svg>
      0418563927
    </p>
  </section>

  <section class="card card-back" aria-label="Business card back">
    <div class="brand-mark"></div>
    <h2 class="business-name">
      <span class="primary">Wollondilly Ridge</span>
      <span class="secondary">Aerial Works</span>
    </h2>
    <p class="services">Antenna installations and repairs Wall mounting of tv’s<br>Additional TV outlets Brolga satellite supply and installations</p>
    <p class="service-areas">Goulburn, Crookwell, Taralga, Tarago, Marulan, Collector, All rural areas</p>
  </section>
</body>
</html>
```